Harbourline Towing website

We need a website design for a towing company based in Australia.
The design should be simple and minimalist. The site can be in colours of the logo are Blue, Red and White (see attached) - but we'd like to see options in some sort of industrial looking metallic theme if possible.
We base our business on our friendly and efficient customer service, the design should attempt to convey this in some way.

Industry/Entity Type

Industrial

Font styles to use
Sans Serif

```html
<!DOCTYPE html>
<html lang="en">
<head>
<meta charset="utf-8">
<title>Harbourline Towing</title>
<link rel="stylesheet" href="https://fonts.googleapis.com/css2?family=Raleway:ital,wght@0,300;0,400;0,500;0,600;1,300&display=swap">
<style>
:root{
  --red:#e10a17;
  --navy:#1d3d73;
  --ink:#1a1a1a;
  --text:#6b6b6b;
  --rule:#b9bec8;
  --band:#d9d9d9;
  --panel:#e6e6e6;
  --black:#000;
  --footer:#111;
  --white:#fff;
}
*{margin:0;padding:0;box-sizing:border-box}
html,body{width:1200px;height:2643px;overflow:hidden;background:var(--white)}
body{position:relative;font-family:"Raleway",sans-serif;color:var(--text)}
.abs{position:absolute}

/* header */
.site-header{position:absolute;left:0;top:0;width:1200px;height:174px;background:#f7f7f7}
.brand{left:92px;top:60px;display:flex;align-items:center;gap:12px}
.brand-mark{width:30px;height:30px;background:var(--navy);border-radius:50%}
.brand-name{font-size:22px;font-weight:600;color:var(--navy)}
.call{left:893px;top:30px;display:flex;gap:12px;align-items:center}
.call-label{font-size:18px;color:var(--red);line-height:1}
.call-number{font-size:26px;color:var(--navy);line-height:1.2}
.main-nav{left:308px;top:132px;display:flex;gap:30px;font-size:19px;color:var(--navy)}
.main-nav a{color:inherit;text-decoration:none;padding-bottom:14px}
.main-nav a.active{color:var(--red);border-bottom:3px solid var(--red)}
.search{left:830px;top:115px;width:282px;height:42px;border:1px solid #ccc;border-radius:6px;background:#efefef;padding:0 12px;display:flex;align-items:center;justify-content:space-between;font-size:15px;color:#aaa}

/* hero */
.hero{position:absolute;left:0;top:174px;width:1200px;height:464px;background:radial-gradient(ellipse at 60% 40%,#fafafa 0%,#e4e4e6 60%,#cfd0d3 100%);box-shadow:0 8px 12px rgba(0,0,0,.18)}
.hero-title{left:115px;top:108px;width:410px;font-size:28px;line-height:38px;font-weight:500;color:var(--ink);white-space:nowrap}
.hero-title span{color:var(--navy)}
.hero-copy{left:115px;top:196px;width:385px;font-size:16px;line-height:25px}
.btn{display:flex;align-items:center;justify-content:center;background:var(--red);color:var(--white);text-decoration:none}
.hero-btn{left:115px;top:295px;width:172px;height:60px;font-size:16px}
.hero-photo{left:537px;top:81px;width:582px;height:274px;background:linear-gradient(180deg,#e8c43a 0%,#c9a21e 55%,#3a3a3a 100%);border-radius:8px}
.round-arrow{width:38px;height:38px;border-radius:50%;background:#222;display:flex;align-items:center;justify-content:center}

/* section heads */
.section-title{display:flex;align-items:center;gap:4px;font-size:45px;font-weight:300;color:var(--navy)}
.section-title::before,.section-title::after{content:"";flex:1;height:1px;background:var(--rule)}
.welcome-title{left:92px;top:745px;width:1018px}
.welcome-title::before{flex:0 0 331px}
.welcome-illus{left:53px;top:863px;width:352px;height:155px;background:linear-gradient(180deg,#f3f3f3 0%,#d81f26 50%,#333 100%);border-radius:10px}
.welcome-copy{left:425px;top:822px;width:685px;font-size:15.5px;line-height:31.5px;font-weight:300}
.more-btn{left:425px;top:997px;width:104px;height:39px;font-size:20px}

.services-title{left:92px;top:1146px;width:1018px}
.service{width:318px}
.service h3{font-size:19px;font-weight:500;color:var(--ink);margin-bottom:14px}
.service .photo{height:224px}
.svc-a{left:92px;top:1245px}
.svc-b{left:440px;top:1245px}
.svc-c{left:793px;top:1245px}
.grey-arrow{width:36px;height:36px;border-radius:50%;background:#a8a8a8;display:flex;align-items:center;justify-content:center}
.all-btn{left:476px;top:1542px;width:243px;height:60px;font-size:25px;font-weight:300}
.services-wrap{position:absolute;left:0;top:1080px;width:1200px;height:555px;box-shadow:0 8px 10px rgba(0,0,0,.12)}

/* what we do / contact */
.band{position:absolute;left:0;top:1737px;width:1200px;height:432px;background:var(--band)}
.what-panel{position:absolute;left:92px;top:1737px;width:622px;height:432px;background:var(--panel)}
.h-big{font-size:45px;font-weight:300;color:var(--ink)}
.what-title{left:93px;top:1672px}
.contact-title{left:745px;top:1672px}
.what-copy{left:131px;top:1772px;width:535px;font-size:16px;line-height:32px;font-weight:300}
.what-list{left:175px;top:1911px;list-style:none;font-size:15.5px;line-height:38px;color:var(--navy)}
.what-list li::before{content:"› ";font-weight:600}
.field{left:788px;width:278px;background:#f4f4f4;border:1px solid #c9c9c9;border-radius:8px;padding:0 14px;font-size:18px;color:#9a9a9a;display:flex;align-items:center}
.field.msg{align-items:flex-start;padding-top:12px}
.submit{left:791px;top:2086px;width:143px;height:43px;background:var(--black);color:var(--white);border-radius:6px;font-size:18px}

/* feedback */
.feedback{position:absolute;left:0;top:2169px;width:1200px;height:333px;background:var(--black)}
.feedback-title{left:0;top:2210px;width:1200px;text-align:center;font-size:37px;font-weight:300;color:var(--white)}
.avatar{width:120px;height:120px;border-radius:50%;border:3px solid var(--white);background:linear-gradient(160deg,#9fb6d6,#3b5b8c)}
.quote{width:335px;font-size:14px;line-height:25.5px;font-style:italic;font-weight:300;color:#666}
.quote b{display:block;font-weight:400;color:#aaa}
.mini-arrow{width:22px;height:24px;background:#333;border:1px solid #777;display:flex;align-items:center;justify-content:center}

/* footer */
.site-footer{position:absolute;left:0;top:2502px;width:1200px;height:141px;background:var(--footer)}
.foot-links{left:97px;top:2531px;font-size:12px;color:#555;word-spacing:2px}
.foot-copy{left:97px;top:2571px;font-size:12px;color:#555}
.social{width:42px;height:42px;border-radius:50%;background:#666;top:2555px}
</style>
</head>
<body>

<header class="site-header">
  <div class="abs brand"><span class="brand-mark"></span><span class="brand-name">Harbourline Towing</span></div>
  <div class="abs call">
    <svg width="38" height="38" viewBox="0 0 38 38"><circle cx="19" cy="19" r="17" fill="none" stroke="#888" stroke-width="2"/><path d="M13 11c2-1 3 3 3 4s-2 1-1 3 3 4 5 5 2-1 3-1 5 1 4 3-2 3-4 3c-6-1-12-7-13-13 0-2 1-3 3-4z" fill="#888"/></svg>
    <div><div class="call-label">Call Us 24/7</div><div class="call-number">1300 555 018</div></div>
  </div>
  <nav class="abs main-nav">
    <a class="active" href="#">Home</a><a href="#">About Us</a><a href="#">Services</a><a href="#">Feedback</a><a href="#">Contact</a>
  </nav>
  <div class="abs search"><span>Search</span>
    <svg width="22" height="22" viewBox="0 0 22 22"><circle cx="9" cy="9" r="6.5" fill="none" stroke="#222" stroke-width="3"/><path d="M14 14l6 6" stroke="#222" stroke-width="3.5" stroke-linecap="round"/></svg>
  </div>
</header>

<section class="hero">
  <h1 class="abs hero-title">We provide<br>Towing services in <span>Australia.</span></h1>
  <p class="abs hero-copy">Lorem ipsum dolor sit amet, consectetur adipisicing elit, sed do eiusmod tempor incididunt ut labore et dolore magna aliqua.</p>
  <a class="abs btn hero-btn" href="#">Know More</a>
  <div class="abs hero-photo" role="img" aria-label="Yellow flatbed tow truck carrying a white car"></div>
  <div class="abs round-arrow" style="left:30px;top:212px"><svg width="14" height="14" viewBox="0 0 14 14"><path d="M9 2L4 7l5 5" fill="none" stroke="#fff" stroke-width="2.5"/></svg></div>
  <div class="abs round-arrow" style="left:1147px;top:212px"><svg width="14" height="14" viewBox="0 0 14 14"><path d="M5 2l5 5-5 5" fill="none" stroke="#fff" stroke-width="2.5"/></svg></div>
</section>

<h2 class="abs section-title welcome-title">Welcome to HLT</h2>
<div class="abs welcome-illus" role="img" aria-label="Illustration of a red tow truck with a boom crane"></div>
<p class="abs welcome-copy">Lorem ipsum dolor sit amet, consectetur adipisicing elit, sed do eiusmod tempor incididunt ut labore et dolore magna aliqua. Ut enim ad minim veniam, quis nostrud exercitation ullamco laboris nisi ut aliquip ex ea commodo consequat. Duis aute irure dolor in reprehenderit in voluptate velit esse cillum dolore eu fugiat nulla pariatur. Excepteur sint occaecat cupidatat non proident, sunt in culpa qui officia deserunt mollit anim.</p>
<a class="abs btn more-btn" href="#">More</a>

<div class="services-wrap"></div>
<h2 class="abs section-title services-title">Our Services</h2>
<div class="abs service svc-a"><h3>Breakdown Vehicle Towing</h3><div class="photo" role="img" aria-label="Tow truck pulling a red car on a city street" style="background:linear-gradient(120deg,#6c6c6c,#b8b8b8 50%,#a3222b)"></div></div>
<div class="abs service svc-b"><h3>Winch &amp; Recovery Service</h3><div class="photo" role="img" aria-label="Off-road vehicle being winched up a rocky slope" style="background:linear-gradient(135deg,#9b8b76,#4a4a4a 55%,#c9b89a)"></div></div>
<div class="abs service svc-c"><h3>Accident Vehicle Towing</h3><div class="photo" role="img" aria-label="Damaged car loaded on a red flatbed truck" style="background:linear-gradient(160deg,#f2f2f2,#9c9c9c 50%,#b5262b)"></div></div>
<div class="abs grey-arrow" style="left:32px;top:1377px"><svg width="12" height="12" viewBox="0 0 12 12"><path d="M8 1L3 6l5 5" fill="none" stroke="#fff" stroke-width="2.5"/></svg></div>
<div class="abs grey-arrow" style="left:1131px;top:1377px"><svg width="12" height="12" viewBox="0 0 12 12"><path d="M4 1l5 5-5 5" fill="none" stroke="#fff" stroke-width="2.5"/></svg></div>
<a class="abs btn all-btn" href="#">View All Services</a>

<div class="band"></div>
<div class="what-panel"></div>
<h2 class="abs h-big what-title">What we do ?</h2>
<h2 class="abs h-big contact-title">Quick Contact</h2>
<p class="abs what-copy">Lorem ipsum dolor sit amet, consectetur adipisicing elit, sed do eiusmod tempor incididunt ut labore et dolore magna aliqua. Ut enim ad minim veniam, quis nostrud exercitation ullamco laboris nisi ut aliquip ex ea commodo consequat.</p>
<ul class="abs what-list">
  <li>Lorem ipsum dolor sit amet,</li>
  <li>consectetur adipisicing elit,</li>
  <li>sed do eiusmod tempor incididunt ut l</li>
  <li>abore et dolore magna aliqua.</li>
  <li>Ut enim ad minim veniam,</li>
</ul>
<div class="abs field" style="top:1773px;height:45px">Name</div>
<div class="abs field" style="top:1838px;height:46px">Phone Number</div>
<div class="abs field" style="top:1894px;height:46px">Address</div>
<div class="abs field msg" style="top:1958px;height:109px">Message</div>
<a class="abs btn submit" href="#">SUBMIT</a>

<section class="feedback"></section>
<h2 class="abs feedback-title">Customer Feedback</h2>
<div class="abs avatar" role="img" aria-label="Portrait of a smiling mechanic in a blue cap" style="left:99px;top:2298px"></div>
<p class="abs quote" style="left:234px;top:2306px">Lorem ipsum dolor sit amet, consectetur adipisicing elit, sed do eiusmod tempor incididunt ut labore et dolore magna aliqua. Ut enim ad minim veniam, quis nostrud exercitation<b>~ Liam Carter</b></p>
<div class="abs avatar" role="img" aria-label="Portrait of a smiling businesswoman" style="left:634px;top:2298px;background:linear-gradient(160deg,#e8e8e8,#555)"></div>
<p class="abs quote" style="left:770px;top:2306px">Lorem ipsum dolor sit amet, consectetur adipisicing elit, sed do eiusmod tempor incididunt ut labore et dolore magna aliqua. Ut enim ad minim veniam, quis nostrud exercitation<b>~ Liam Carter</b></p>
<div class="abs mini-arrow" style="left:1047px;top:2465px"><svg width="8" height="10" viewBox="0 0 8 10"><path d="M6 1L2 5l4 4" fill="none" stroke="#ccc" stroke-width="1.5"/></svg></div>
<div class="abs mini-arrow" style="left:1078px;top:2465px"><svg width="8" height="10" viewBox="0 0 8 10"><path d="M2 1l4 4-4 4" fill="none" stroke="#ccc" stroke-width="1.5"/></svg></div>

<footer class="site-footer"></footer>
<div class="abs foot-links">Home &nbsp;About Us &nbsp;Services &nbsp;Feedback &nbsp;Contact</div>
<div class="abs foot-copy">All Rights Reserved, copyrights @2014</div>
<div class="abs social" style="left:918px"></div>
<div class="abs social" style="left:971px"></div>
<div class="abs social" style="left:1019px"></div>
<div class="abs social" style="left:1070px"></div>

</body>
</html>
```